INNOVATION WEBSITE NEEDED: Agency from NZ needs YOU

Please see the enclosed documents for a detailed brief. It needs to be clean / simple / elegant / premium looking - that will appeal to companies that range from start-up to multi-national!
Note:
Perhaps instead of an actual shop, people can press an 'enquire now' button?

Target Market(s)

Start ups to multi-nationals

Industry/Entity Type

Marketing

Number of Pages Required

5+ page

Requirements
Must have
• Wordpress
• SEO
• Format friendly (mobile / tablet / etc)
• I have the URL: www.qu-tessaroly.com - I would like a working website. Please let me know what else you require to 'go live' with. Thanks!
Nice to have
• Please use / improve on my current ideas
• Perhaps use my logo icon (in different colours) for each 'product'?

```html
<!DOCTYPE html>
<html lang="en">
<head>
<meta charset="utf-8">
<title>Qu-Tessaroly – Delivering Big Ideas, Fast and Affordable</title>
<link rel="stylesheet" href="https://fonts.googleapis.com/css2?family=Cinzel:wght@400;700&family=Open+Sans:wght@400;600;700&display=swap">
<style>
:root{
  --navy:#2b2a6b;
  --blue:#0f8fd6;
  --blue-btn:#1f97d4;
  --ink:#222;
  --text:#333;
  --muted:#666;
  --grey-band:#f1f1f1;
  --card-grey:#f2f2f2;
  --footer:#3e4b5d;
  --footer-field:#4e5b6e;
  --footer-text:#e6e9ee;
  --accent:#4a1fb8;
  --white:#fff;
}
*{box-sizing:border-box;margin:0;padding:0}
html,body{width:1200px;height:4489px;overflow:hidden}
body{position:relative;background:var(--white);font-family:"Open Sans",Arial,sans-serif;color:var(--text);font-size:15px;line-height:1.45}
.abs{position:absolute}
.art{position:absolute;border-radius:2px}

/* header */
.site-header{position:absolute;left:0;top:0;width:1200px;height:120px;background:var(--white);border-bottom:1px solid #e4e4e4}
.brand{position:absolute;left:50px;top:18px;display:flex;align-items:center;gap:12px}
.brand-dot{width:44px;height:44px;border-radius:50%;background:var(--navy)}
.brand-name{font-family:"Open Sans",Arial,sans-serif;font-weight:700;font-size:31px;color:var(--navy);letter-spacing:.5px}
.brand-tag{position:absolute;left:106px;top:62px;font-size:11px;letter-spacing:3px;color:var(--muted)}
.contact-strip{position:absolute;top:14px;right:40px;display:flex;gap:40px;font-size:14px;color:var(--text);line-height:1.35}
.contact-item{display:flex;gap:10px;align-items:flex-start}
.main-nav{position:absolute;right:40px;top:92px;display:flex;gap:58px;font-size:15px;color:var(--ink)}
.main-nav a{color:inherit;text-decoration:none;padding-bottom:9px}
.main-nav a.active{border-bottom:3px solid var(--navy)}

/* hero */
.hero{position:absolute;left:0;top:120px;width:1200px;height:535px;background:linear-gradient(90deg,#cfd0d1 0%,#e4e4e3 45%,#dadada 100%)}
.hero-title{position:absolute;left:745px;top:118px;width:420px;font-family:"Cinzel",Georgia,serif;font-size:35px;line-height:1.15;color:var(--ink);letter-spacing:1px}
.btn-contact{position:absolute;left:745px;top:292px;width:158px;height:50px;background:var(--navy);color:var(--white);font-family:"Cinzel",Georgia,serif;font-size:17px;letter-spacing:1px;display:flex;align-items:center;justify-content:center}

/* pricing teaser */
.plans{position:absolute;left:0;top:655px;width:1200px;height:312px;border-bottom:3px solid #dcdcdc}
.plan{position:absolute;top:53px;width:240px;height:162px;background:var(--navy);color:var(--white);text-align:center;font-family:"Cinzel",Georgia,serif}
.plan-name{height:46px;border-bottom:1px solid rgba(255,255,255,.25);font-size:19px;letter-spacing:1px;padding-top:10px}
.plan-price{font-size:32px;margin-top:28px;letter-spacing:1px}
.plan-plus{font-size:56px;line-height:1;margin-top:14px;font-family:"Open Sans",Arial,sans-serif;font-weight:400}
.plan-btn{position:absolute;left:50%;transform:translateX(-50%);top:152px;width:128px;height:42px;background:var(--blue-btn);color:var(--white);font-size:16px;letter-spacing:1px;display:flex;align-items:center;justify-content:center}

/* content rows */
.band{position:absolute;left:0;width:1200px}
.band.grey{background:var(--grey-band)}
.h-section{font-family:"Cinzel",Georgia,serif;font-size:33px;color:var(--ink);letter-spacing:2px;font-weight:400}
.copy{font-size:15px;line-height:1.5;color:var(--text)}
.copy p{margin:0}

/* shop */
.shop{top:2424px;height:1011px;background:var(--grey-band)}
.center-title{position:absolute;left:0;width:1200px;text-align:center}
.product{position:absolute;width:264px;text-align:center}
.product-face{position:absolute;left:0;width:264px;background:var(--white)}
.coin{position:absolute;left:50%;transform:translateX(-50%);width:134px;height:134px;border-radius:50%;background:var(--navy);border:5px solid var(--blue);color:var(--white);font-size:82px;font-weight:700;display:flex;align-items:center;justify-content:center;font-family:"Open Sans",Arial,sans-serif}
.product-name{position:absolute;left:0;width:264px;font-size:16px;color:var(--ink)}
.product-body{position:absolute;left:0;width:264px;background:var(--blue);color:var(--white);padding:0 16px}
.product-price{font-family:"Cinzel",Georgia,serif;font-size:34px;margin-top:14px;line-height:1.2}
.product-text{font-size:12.5px;font-weight:600;line-height:1.45;margin-top:6px}

/* team */
.team-intro{position:absolute;left:90px;top:3552px;width:1020px;font-size:14px;text-align:center;line-height:1.5}
.member{position:absolute;top:3636px;width:240px;height:354px;background:var(--card-grey);text-align:center}
.avatar{width:120px;height:120px;border-radius:50%;margin:18px auto 0;background:linear-gradient(160deg,#b9b2aa,#6f6660)}
.member-name{font-size:22px;color:var(--ink);margin-top:22px}
.member-bio{font-size:13px;color:var(--muted);line-height:1.5;margin:12px 22px 0}
.member-links{display:flex;justify-content:center;gap:22px;margin-top:28px}
.member-links span{width:14px;height:14px;border-radius:50%;background:var(--navy)}

/* footer */
.site-footer{position:absolute;left:0;top:4035px;width:1200px;height:454px;background:var(--footer);color:var(--footer-text);font-size:13.5px;line-height:1.5}
.f-col{position:absolute;top:42px}
.f-head{font-size:18px;font-weight:700;color:var(--white);margin-bottom:18px}
.f-rule{width:40px;height:2px;background:var(--blue);margin:22px 0 20px}
.f-row{display:flex;gap:14px;align-items:flex-start;margin-bottom:16px}
.f-link{color:#6fb6ee}
.f-social{display:flex;gap:14px;margin-top:4px}
.f-social span{width:22px;height:22px;border-radius:50%;background:var(--blue)}
.field-label{font-size:13px;margin-bottom:6px}
.field{width:320px;height:40px;background:var(--footer-field);margin-bottom:16px}
.field.tall{height:92px}
.btn-send{width:162px;height:40px;background:var(--accent);color:var(--white);font-size:13px;font-weight:700;letter-spacing:.5px;display:flex;align-items:center;justify-content:center}
</style>
</head>
<body>

<header class="site-header">
  <div class="brand"><span class="brand-dot"></span><span class="brand-name">Qu-Tessaroly</span></div>
  <div class="brand-tag">CREATING THE FUTURE</div>
  <div class="contact-strip">
    <div class="contact-item">
      <svg width="22" height="22" viewBox="0 0 24 24" aria-hidden="true"><circle cx="12" cy="12" r="12" fill="#2b2a6b"/><path d="M8.5 6.5l2 2-1.2 1.6c.8 1.6 2 2.8 3.6 3.6l1.6-1.2 2 2-1.4 1.6c-3.6-.4-7.8-4.6-8.2-8.2z" fill="#fff"/></svg>
      <div>004 218 6650<br>info@example.com</div>
    </div>
    <div class="contact-item">
      <svg width="20" height="26" viewBox="0 0 20 26" aria-hidden="true"><path d="M10 0C4.5 0 0 4.4 0 9.8 0 17 10 26 10 26s10-9 10-16.2C20 4.4 15.5 0 10 0z" fill="#2b2a6b"/><circle cx="10" cy="9.5" r="3.6" fill="#fff"/></svg>
      <div>72 Harbour Lane<br>Wellford, WL 40312</div>
    </div>
  </div>
  <nav class="main-nav">
    <a class="active">Home</a><a>Shop</a><a>Our Purpose</a><a>What We Do</a><a>The Team</a><a>Contact</a>
  </nav>
</header>

<section class="hero">
  <div class="art" style="left:0;top:0;width:700px;height:535px;background:linear-gradient(90deg,#c4c5c6,#dcdcdb)" role="img" aria-label="Businessman sketching ideas, charts and a city skyline on a wall"></div>
  <h1 class="hero-title">Qu-Tessaroly:<br>Delivering Big Ideas,<br>Fast and<br>Affordable</h1>
  <div class="btn-contact">CONTACT</div>
</section>

<section class="plans">
  <div class="plan" style="left:51px"><div class="plan-name">The 'Barista'</div><div class="plan-price">$FREE</div><div class="plan-btn">BUY NOW</div></div>
  <div class="plan" style="left:330px"><div class="plan-name">The 'Trailblazer'</div><div class="plan-price">$499</div><div class="plan-btn">BUY NOW</div></div>
  <div class="plan" style="left:621px"><div class="plan-name">The 'Ninja'</div><div class="plan-price">$749</div><div class="plan-btn">BUY NOW</div></div>
  <div class="plan" style="left:909px"><div class="plan-name">More Options</div><div class="plan-plus">+</div><div class="plan-btn">CLICK NOW</div></div>
</section>

<section class="band grey" style="top:969px;height:366px">
  <h2 class="h-section abs" style="left:90px;top:48px">Re-Boot or Kick-Start...?</h2>
  <div class="copy abs" style="left:90px;top:106px;width:560px">
    <p>Do you need to reboot or kick-start your company's innovation capabilities in terms of process, people or projects?</p>
    <p><strong>Do you need:</strong></p>
    <p>- &nbsp;&nbsp;a new way of doing something?</p>
    <p>- &nbsp;&nbsp;a brilliant breakthrough idea?</p>
    <p>- &nbsp;&nbsp;a 3-5 year roadmap of strategic innovation?</p>
    <p>Or simply a new perspective to jump start the team?</p>
    <p>If you have answered yes to any of the above, contact Qu-Tessaroly!</p>
    <p>We create innovation that hits the bottom line.</p>
  </div>
  <div class="art" style="left:660px;top:20px;width:495px;height:330px;background:linear-gradient(135deg,#ffffff,#e9e9e0)" role="img" aria-label="Hand drawing a content strategy flow from create to publish"></div>
</section>

<section class="band" style="top:1335px;height:360px">
  <div class="art" style="left:105px;top:30px;width:405px;height:285px;background:linear-gradient(160deg,#f4f4f4,#d9d9d9)" role="img" aria-label="Hand drawing ideas rising from an open book"></div>
  <h2 class="h-section abs" style="left:567px;top:40px">Our Purpose</h2>
  <div class="copy abs" style="left:567px;top:102px;width:580px">
    <p>Our purpose is to re-define how companies like yours get great innovation. Quickly.</p>
    <p>&nbsp;</p>
    <p>The team at Qu-Tessaroly have worked both client side and as consultants. We know what works and how things tick internally. It's not just about pretty pictures. Ideas need to stack up: strategically, culturally and commercially.</p>
    <p>&nbsp;</p>
    <p>We get that. We can help you achieve that. That's our purpose.</p>
  </div>
</section>

<section class="band grey" style="top:1695px;height:360px">
  <h2 class="h-section abs" style="left:75px;top:22px">What We Do</h2>
  <div class="copy abs" style="left:75px;top:74px;width:640px">
    <p><strong>We innovate. For you.</strong></p>
    <p>The most common things we hear are:</p>
    <p>- &nbsp;&nbsp;"I need a breakthrough innovation, but am staring at a blank piece of paper"</p>
    <p>- &nbsp;&nbsp;"I have to come up with a great idea, but have a limited budget and little time"</p>
    <p>- &nbsp;&nbsp;"It's hard to get all the different functions and people aligned – so we're getting no where on innovation"</p>
    <p>That's where we can help. We've been there and done that…many times. What we do is:</p>
    <p>- &nbsp;&nbsp;Deliver big ideas!</p>
    <p>- &nbsp;&nbsp;Fast and affordable</p>
    <p>- &nbsp;&nbsp;Get buy-in at all levels.</p>
  </div>
  <div class="art" style="left:765px;top:95px;width:390px;height:250px;background:linear-gradient(135deg,#f7f7f7,#dedede)" role="img" aria-label="Hand touching a cluster of drawn gears labelled marketing"></div>
</section>

<section class="band" style="top:2055px;height:369px">
  <div class="art" style="left:105px;top:30px;width:360px;height:240px;background:linear-gradient(135deg,#f6d27a,#8ecbe8 50%,#e58aa8)" role="img" aria-label="Colourful speech bubbles around the word marketing"></div>
  <h2 class="h-section abs" style="left:510px;top:40px">How It Works</h2>
  <div class="copy abs" style="left:510px;top:98px;width:640px">
    <p>Instead of asking for a quote like with most agencies, we have a price list. You can order our services online!</p>
    <p>There's no back and forwards with long winded quotes that have taken your briefing, reworded it and sent it back to you with a huge price tag attached!</p>
    <p>Simply have a look at our innovation shop window and if you like what you see and know exactly what you want, you push the 'Buy' button. And then we will start working.</p>
    <p>If you want to talk beforehand, simply give the team at Qu-Tessaroly a call and we can have a quick chat first.</p>
  </div>
</section>

<section class="band shop">
  <h2 class="h-section center-title" style="top:48px">Innovation Shop</h2>

  <div class="product" style="left:51px;top:111px">
    <div class="product-face" style="top:60px;height:120px"></div>
    <div class="coin" style="top:0">$</div>
    <div class="product-name" style="top:150px">'The Barista'</div>
    <div class="product-body" style="top:180px;height:213px"><div class="product-price">FREE</div><div class="product-text">Free 15 Minute Chat<br>A sounding board &amp; feedback to your job that needs to be done.<br>We challenge and build any ideas you already have in mind</div></div>
  </div>
  <div class="product" style="left:330px;top:111px">
    <div class="product-face" style="top:60px;height:120px"></div>
    <div class="coin" style="top:0">$</div>
    <div class="product-name" style="top:150px">'The Trailblazer'</div>
    <div class="product-body" style="top:180px;height:213px"><div class="product-price">$499</div><div class="product-text">Free 15 Minute Chat<br>A sounding board &amp; feedback to your job that needs to be done.<br>We challenge and build any ideas you already have in mind</div></div>
  </div>
  <div class="product" style="left:612px;top:111px">
    <div class="product-face" style="top:60px;height:120px"></div>
    <div class="coin" style="top:0">$</div>
    <div class="product-name" style="top:150px">'The Ninja'</div>
    <div class="product-body" style="top:180px;height:213px"><div class="product-price">$749</div><div class="product-text">Free 15 Minute Chat<br>A sounding board &amp; feedback to your job that needs to be done.<br>We challenge and build any ideas you already have in mind</div></div>
  </div>
  <div class="product" style="left:894px;top:111px">
    <div class="product-face" style="top:60px;height:120px"></div>
    <div class="coin" style="top:0">$</div>
    <div class="product-name" style="top:150px">'The Maverick'</div>
    <div class="product-body" style="top:180px;height:213px"><div class="product-price">$949</div><div class="product-text">Free 15 Minute Chat<br>A sounding board &amp; feedback to your job that needs to be done.<br>We challenge and build any ideas you already have in mind</div></div>
  </div>

  <div class="product" style="left:51px;top:597px">
    <div class="product-face" style="top:60px;height:104px"></div>
    <div class="coin" style="top:0">$</div>
    <div class="product-name" style="top:138px">'The Mastermind'</div>
    <div class="product-body" style="top:164px;height:211px"><div class="product-price">$2499</div><div class="product-text">Free 15 Minute Chat<br>A sounding board &amp; feedback to your job that needs to be done.<br>We challenge and build any ideas you already have in mind</div></div>
  </div>
  <div class="product" style="left:330px;top:597px">
    <div class="product-face" style="top:60px;height:104px"></div>
    <div class="coin" style="top:0">$</div>
    <div class="product-name" style="top:138px">Workshop I: Gold Class</div>
    <div class="product-body" style="top:164px;height:211px"><div class="product-price">$3,499</div><div class="product-text">Free 15 Minute Chat<br>A sounding board &amp; feedback to your job that needs to be done.<br>We challenge and build any ideas you already have in mind</div></div>
  </div>
  <div class="product" style="left:612px;top:597px">
    <div class="product-face" style="top:60px;height:104px"></div>
    <div class="coin" style="top:0">$</div>
    <div class="product-name" style="top:138px">Workshop II: Platinum Class</div>
    <div class="product-body" style="top:164px;height:211px"><div class="product-price">$4,999</div><div class="product-text">Free 15 Minute Chat<br>A sounding board &amp; feedback to your job that needs to be done.<br>We challenge and build any ideas you already have in mind</div></div>
  </div>
  <div class="product" style="left:894px;top:597px">
    <div class="product-face" style="top:60px;height:104px"></div>
    <div class="coin" style="top:0">$</div>
    <div class="product-name" style="top:138px">Workshop III: Diamond Class</div>
    <div class="product-body" style="top:164px;height:211px"><div class="product-price">$7,999</div><div class="product-text">Free 15 Minute Chat<br>A sounding board &amp; feedback to your job that needs to be done.<br>We challenge and build any ideas you already have in mind</div></div>
  </div>
</section>

<section class="team">
  <h2 class="h-section center-title" style="top:3470px">The Team</h2>
  <p class="team-intro">We are a small team driven by innovation and focused on action. Leveraging an innovative approach to team set up, we can call on a vast array of skilled team members depending on the assignment. Tapping into a worldwide network of highly skilled consultants, there is no project we can't handle.</p>
  <div class="member" style="left:63px"><div class="avatar" role="img" aria-label="Portrait of team member"></div><div class="member-name">Rina Valde</div><p class="member-bio">Personalized trial access rcises, amin ders malesuada id dolor non, elemen tum auctor arcu. Cras consectet</p><div class="member-links"><span></span><span></span><span></span><span></span></div></div>
  <div class="member" style="left:330px"><div class="avatar" role="img" aria-label="Portrait of team member"></div><div class="member-name">Rina Valde</div><p class="member-bio">Personalized trial access rcises, amin ders malesuada id dolor non, elemen tum auctor arcu. Cras consectet</p><div class="member-links"><span></span><span></span><span></span><span></span></div></div>
  <div class="member" style="left:615px"><div class="avatar" role="img" aria-label="Portrait of team member"></div><div class="member-name">Rina Valde</div><p class="member-bio">Personalized trial access rcises, amin ders malesuada id dolor non, elemen tum auctor arcu. Cras consectet</p><div class="member-links"><span></span><span></span><span></span><span></span></div></div>
  <div class="member" style="left:897px"><div class="avatar" role="img" aria-label="Portrait of team member"></div><div class="member-name">Rina Valde</div><p class="member-bio">Personalized trial access rcises, amin ders malesuada id dolor non, elemen tum auctor arcu. Cras consectet</p><div class="member-links"><span></span><span></span><span></span><span></span></div></div>
</section>

<footer class="site-footer">
  <div class="f-col" style="left:126px;width:270px">
    <div class="f-head">About Us</div>
    <p>Far far away, behind the word mountains, far from the countries Vokalia and Consonantia, Separated they live in Bookmarksgrove right at the coast of the Semantics.</p>
    <div class="f-rule"></div>
    <p>© 2016 Qu-Tessaroly.<br>All Rights Reserved</p>
  </div>
  <div class="f-col" style="left:450px;width:250px">
    <div class="f-head">Our Address</div>
    <div class="f-row"><svg width="14" height="18" viewBox="0 0 20 26" aria-hidden="true"><path d="M10 0C4.5 0 0 4.4 0 9.8 0 17 10 26 10 26s10-9 10-16.2C20 4.4 15.5 0 10 0z" fill="#0f8fd6"/><circle cx="10" cy="9.5" r="3.6" fill="#3e4b5d"/></svg><span>41 Kelmore Road, Suite 12<br>Wellford WL 40318</span></div>
    <div class="f-row"><svg width="16" height="16" viewBox="0 0 24 24" aria-hidden="true"><path d="M5 3l4 4-2.4 3.2c1.6 3.2 4 5.6 7.2 7.2L17 15l4 4-2.8 3.2C11 21.4 2.6 13 1.8 5.8z" fill="#0f8fd6"/></svg><span>+ 4471 8820 36</span></div>
    <div class="f-row"><svg width="16" height="14" viewBox="0 0 24 18" aria-hidden="true"><rect x="0" y="0" width="24" height="18" rx="2" fill="#0f8fd6"/><path d="M1 1l11 9 11-9" stroke="#3e4b5d" stroke-width="2" fill="none"/></svg><span class="f-link">hello@qu-tessaroly.com</span></div>
    <div class="f-row"><svg width="16" height="16" viewBox="0 0 24 24" aria-hidden="true"><circle cx="12" cy="12" r="10" stroke="#0f8fd6" stroke-width="2.4" fill="none"/><path d="M2 12h20M12 2c4 4 4 16 0 20M12 2c-4 4-4 16 0 20" stroke="#0f8fd6" stroke-width="1.8" fill="none"/></svg><span class="f-link">www.qu-tessaroly.com</span></div>
    <div class="f-head" style="margin-top:20px;margin-bottom:12px">Connect with Us</div>
    <div class="f-social"><span></span><span></span><span></span><span></span></div>
  </div>
  <div class="f-col" style="left:729px;width:340px">
    <div class="f-head">Drop us a line</div>
    <div class="field-label">Name</div><div class="field"></div>
    <div class="field-label">E-mail</div><div class="field"></div>
    <div class="field-label">Message</div><div class="field tall"></div>
    <div class="btn-send">SEND MESSAGE</div>
  </div>
</footer>

</body>
</html>
```